CREST BLEND 250

Hi our company name is Maple Hollow Foods and we are operating with the same brand and we have shared a logo file for the same in this attachment. We a need to design a cover for our product CREST BLEND which is a mixture of dry fruits (almond, pista etc...), nuts (brazil nut, hazel nut etc...), seeds (pumpkin seed, sunflower seed etc....), berries (dried cranberry, dried blueberry etc....) we need the design for the same....
The packaging details like the date of packing , batch details, expiry and bar code will be on sticker which is of size 3.5 cm width and 4.5 cm height... this is only sticker which be used externally to pasted so need a space left for this...preferably on the back side bottom....
The cover is kraft paper stand up pouch which has no window
The cover size is 16CM WIDTH *23CM HEIGHT
The printable area of the cover is 14CM WIDTH *17 CM HEIGHT
(wastage on top side is 4.5 cm and from bottom is 1.5cm
from both left and right side is 1cm equally)
*sample previous design to have a cover idea and copy of logo
* printing doesn't allow to have minute details
*some other sample designs which are used by other players on the same pouch
Colors
Designer to choose colors to be used in the design.
Requirements
Must have
- THERE WILL BE A NUTRITIONAL DATA COLUMN ALSO TO BE THERE WHICH IN WORK WITH THE DEPARTMENT...JUST NEED TO PROVIDE A SPACE FOR THAT WHICH CAN BE IN ANY STANDARD FORMAT...

```html
<!DOCTYPE html>
<html lang="en">
<head>
<meta charset="utf-8">
<title>Crest Blend – Pouch Front</title>
<link rel="stylesheet" href="https://fonts.googleapis.com/css2?family=Barlow+Condensed:wght@500;600&family=Barlow+Semi+Condensed:wght@600&display=swap">
<style>
  :root {
    --crimson: #d6174f;
    --card: #ffffff;
    --ghost: #f3e6d6;
    --slate: #7a9593;
    --slate-text: #6b8280;
    --gold: #f2b632;
    --brand: #5b1717;
    --nut-light: #c9a27a;
    --nut-dark: #8a5a3c;
  }
  html, body {
    margin: 0;
    padding: 0;
    width: 1200px;
    height: 1000px;
    overflow: hidden;
    background: var(--crimson);
  }
  .canvas {
    position: relative;
    width: 1200px;
    height: 1000px;
    background: var(--crimson);
  }
  .pouch-front {
    position: absolute;
    left: 248px;
    top: 48px;
    width: 704px;
    height: 904px;
    background: var(--card);
    overflow: hidden;
    box-shadow: 0 10px 28px rgba(90, 0, 25, 0.35);
    font-family: "Barlow Condensed", sans-serif;
  }
  .ghost-name {
    position: absolute;
    left: -20px;
    width: 760px;
    text-align: center;
    font-weight: 600;
    color: transparent;
    -webkit-text-stroke: 2px var(--ghost);
    line-height: 1;
    letter-spacing: -4px;
    white-space: nowrap;
  }
  .ghost-name.top { top: -20px; font-size: 420px; }
  .ghost-name.bottom { top: 370px; font-size: 470px; }
  .brand {
    position: absolute;
    top: 118px;
    left: 0;
    width: 704px;
    text-align: center;
  }
  .brand-dot {
    display: block;
    width: 22px;
    height: 22px;
    margin: 0 auto 10px;
    border-radius: 50%;
    background: var(--brand);
  }
  .brand-name {
    font-family: "Barlow Condensed", sans-serif;
    font-weight: 600;
    font-size: 30px;
    line-height: 1;
    color: var(--brand);
  }
  .ribbon {
    position: absolute;
    left: 539px;
    top: 0;
    width: 88px;
    height: 207px;
  }
  .ribbon-label {
    position: absolute;
    left: 539px;
    top: 150px;
    width: 88px;
    text-align: center;
    font-family: "Barlow Semi Condensed", sans-serif;
    font-weight: 600;
    font-size: 34px;
    color: #ffffff;
  }
  .product-name {
    position: absolute;
    left: 0;
    width: 704px;
    margin: 0;
    text-align: center;
    font-weight: 500;
    color: var(--crimson);
    line-height: 1;
    white-space: nowrap;
  }
  .product-name.line-one { top: 203px; font-size: 200px; }
  .product-name.line-two { top: 345px; font-size: 235px; }
  .contents {
    position: absolute;
    left: 90px;
    top: 606px;
    width: 522px;
    height: 38px;
    border-top: 3px solid var(--gold);
    border-bottom: 3px solid var(--gold);
    display: flex;
    justify-content: center;
    align-items: center;
    gap: 24px;
    font-family: "Barlow Semi Condensed", sans-serif;
    font-weight: 600;
    font-size: 29px;
    color: var(--slate-text);
    letter-spacing: 0.3px;
    background: var(--card);
  }
  .product-visual {
    position: absolute;
    left: 107px;
    top: 668px;
    width: 490px;
    height: 186px;
  }
</style>
</head>
<body>
<div class="canvas">
  <section class="pouch-front">
    <div class="ghost-name top" aria-hidden="true">CREST</div>
    <div class="ghost-name bottom" aria-hidden="true">BLEND</div>

    <div class="brand">
      <span class="brand-dot"></span>
      <div class="brand-name">Maple Hollow Foods</div>
    </div>

    <svg class="ribbon" viewBox="0 0 88 207" aria-hidden="true">
      <polygon points="0,0 88,0 88,207 44,190 0,207" fill="var(--slate)"/>
    </svg>
    <div class="ribbon-label">NEW</div>

    <h1 class="product-name line-one">CREST</h1>
    <h1 class="product-name line-two">BLEND</h1>

    <div class="contents">
      <span>DRY FRUITS</span><span>NUTS</span><span>SEEDS</span><span>BERRIES</span>
    </div>

    <svg class="product-visual" viewBox="0 0 490 186" role="img" aria-label="Close-up photo of the blend: almonds, pumpkin seeds, dried cranberries and blueberries">
      <defs>
        <linearGradient id="mix-tone" x1="0" y1="0" x2="1" y2="1">
          <stop offset="0" stop-color="var(--nut-light)"/>
          <stop offset="0.5" stop-color="#b98a6a"/>
          <stop offset="1" stop-color="var(--nut-dark)"/>
        </linearGradient>
      </defs>
      <path d="M0,0 H490 V140 Q490,162 466,162 Q448,162 440,176 Q434,186 418,186 H72 Q56,186 50,176 Q42,162 24,162 Q0,162 0,140 Z" fill="url(#mix-tone)"/>
    </svg>
  </section>
</div>
</body>
</html>
```